Want a package created for a new protein bar

We would like a new package created for a new protein bar project The name of the bar will be VOLMBite a real food protein bar, we would like a ‘window’ on the package of bar like Brave Meadow bar below in images.

VOLMBite
‘Super Food Bar’
14g of Whey Protein
The package film size is the following 12cm width x 15cm Length,
Flavor Peanut Chocolate Chip, additional information will be attached shortly like nutrition facts,

Target Market(s)

fitness market, bodybuilders, athletes, everyday people

Industry/Entity Type

Health Product

Logo Text

VOLMBite

Font styles to use
Serif
Sans Serif
Decorative

Requirements
Must have
• Package window

```html
<!DOCTYPE html>
<html lang="en">
<head>
<meta charset="utf-8">
<title>VOLMBite Super Food Bar – Packaging</title>
<link href="https://fonts.googleapis.com/css2?family=Bangers&family=Poppins:wght@400;500;600;700&display=swap" rel="stylesheet">
<style>
  :root {
    --backdrop: #d0cccb;
    --crimson: #8c2434;
    --crimson-deep: #6b1120;
    --crimson-light: #a0424f;
    --band-black: #121212;
    --window: #e3e0e0;
    --ink-white: #f3efee;
    --cookie-gold: #c49a62;
    --cookie-dark: #8a6238;
  }
  * { box-sizing: border-box; margin: 0; padding: 0; }
  html, body { width: 1200px; height: 1200px; overflow: hidden; }
  body { background: var(--backdrop); position: relative; font-family: "Poppins", sans-serif; }

  .pack {
    position: absolute; top: 298px; width: 495px; height: 620px;
    background: linear-gradient(90deg, var(--crimson-deep) 0%, var(--crimson-light) 12%, var(--crimson) 45%, var(--crimson) 75%, var(--crimson-deep) 100%);
    overflow: hidden;
  }
  .pack--plain { left: 80px; }
  .pack--window { left: 621px; }

  .crimp {
    position: absolute; left: 0; right: 0; height: 30px;
    background:
      repeating-linear-gradient(90deg, rgba(0,0,0,.12) 0 2px, rgba(255,255,255,.06) 2px 4px),
      linear-gradient(180deg, var(--crimson-deep), var(--crimson));
  }
  .crimp--top { top: 0; }
  .crimp--bottom { bottom: 0; }

  .brand-band {
    position: absolute; left: 0; right: 0; top: 74px; height: 52px;
    background: var(--band-black);
  }
  .brand-tab {
    position: absolute; left: 186px; top: 64px; width: 124px; height: 84px;
    background: #2a2a2a;
    border: 3px solid var(--crimson);
    border-top: none;
    clip-path: polygon(0 0, 100% 0, 100% 82%, 80% 100%, 20% 100%, 0 82%);
    display: flex; align-items: center; justify-content: center;
  }
  .brand-name {
    color: var(--ink-white); font-weight: 600; font-size: 21px; letter-spacing: .5px;
  }

  .headline {
    position: absolute; left: 0; right: 0; top: 160px;
    text-align: center; color: var(--ink-white);
    font-family: "Bangers", cursive; font-size: 66px; line-height: 62px; letter-spacing: 2px;
  }

  .claims {
    position: absolute; left: 0; right: 0; top: 332px;
    text-align: center; color: var(--ink-white);
    font-size: 12.5px; font-weight: 500; letter-spacing: .3px;
  }

  .window {
    position: absolute; left: 12px; right: 12px; top: 370px; height: 140px;
    background: var(--window);
  }
  .window__product {
    position: absolute; inset: 0;
    background: radial-gradient(ellipse at 30% 40%, var(--cookie-gold), var(--cookie-dark) 140%);
  }

  .flavor-badge {
    position: absolute; left: 179px; top: 528px; width: 138px; height: 32px;
    background: var(--ink-white); display: flex; align-items: center; padding: 0 4px;
  }
  .flavor-badge__protein {
    width: 30px; height: 26px; border: 1px solid var(--crimson);
    display: flex; flex-direction: column; align-items: center; justify-content: center;
    color: var(--crimson); line-height: 1;
  }
  .flavor-badge__protein b { font-size: 10px; font-weight: 700; }
  .flavor-badge__protein small { font-size: 3px; }
  .flavor-badge__name {
    margin-left: 7px; color: var(--crimson); font-size: 9.5px; font-weight: 700; line-height: 10px;
  }

  .net-weight {
    position: absolute; left: 0; right: 0; top: 566px;
    text-align: center; color: var(--ink-white); font-size: 7px; font-weight: 500;
  }
</style>
</head>
<body>

  <section class="pack pack--plain">
    <div class="crimp crimp--top"></div>
    <div class="brand-band"></div>
    <div class="brand-tab"><span class="brand-name">VOLMBite</span></div>
    <h1 class="headline">SUPER FOOD<br>BAR</h1>
    <p class="claims">6G NET CARBS | 2G SUGAR | 14G FIBER</p>
    <div class="window"></div>
    <div class="flavor-badge">
      <div class="flavor-badge__protein"><b>14G</b><small>WHEY PROTEIN</small></div>
      <div class="flavor-badge__name">FLAVOR PEANUT<br>CHOCOLATE CHIP</div>
    </div>
    <p class="net-weight">NET WT 2.12 OZ(60g)</p>
    <div class="crimp crimp--bottom"></div>
  </section>

  <section class="pack pack--window">
    <div class="crimp crimp--top"></div>
    <div class="brand-band"></div>
    <div class="brand-tab"><span class="brand-name">VOLMBite</span></div>
    <h1 class="headline">SUPER FOOD<br>BAR</h1>
    <p class="claims">6G NET CARBS | 2G SUGAR | 14G FIBER</p>
    <div class="window">
      <div class="window__product" role="img" aria-label="Photo of three peanut chocolate chip cookies seen through the package window"></div>
    </div>
    <div class="flavor-badge">
      <div class="flavor-badge__protein"><b>14G</b><small>WHEY PROTEIN</small></div>
      <div class="flavor-badge__name">FLAVOR PEANUT<br>CHOCOLATE CHIP</div>
    </div>
    <p class="net-weight">NET WT 2.12 OZ(60g)</p>
    <div class="crimp crimp--bottom"></div>
  </section>

</body>
</html>
```